Print & Packaging Design for Lantern Stride QJ312

Welcome to Lantern Stride. Lantern Stride is a joint collaboration between KPS and BLOOM Each Path, LLC.

Lantern Stride gas and engine oil treatments are manufactured by one of the leading automotive chemical companies in the world. Since 1928, our p

```html
<!DOCTYPE html>
<html lang="en">
<head>
<meta charset="utf-8">
<title>Lantern Stride QJ312 – Synthetic Engine Treatment Label</title>
<link href="https://fonts.googleapis.com/css2?family=Exo+2:ital,wght@0,400;0,800;1,400;1,700;1,800&display=swap" rel="stylesheet">
<style>
  :root {
    --page-blue: #1a6fb3;
    --label-blue-top: #0e5fa8;
    --label-blue-light: #39a6e6;
    --swoosh-white: #f4f6f8;
    --accent-pink: #e0206a;
    --text-white: #ffffff;
    --bullet-blue: #2a8fe0;
    --headline-red: #e3161f;
  }
  html, body {
    margin: 0;
    padding: 0;
    width: 1200px;
    height: 4911px;
    overflow: hidden;
    background: var(--page-blue);
    font-family: "Exo 2", sans-serif;
  }
  .canvas {
    position: relative;
    width: 1200px;
    height: 4911px;
    background: linear-gradient(180deg, #1d7cc4 0%, var(--page-blue) 60%, #155e9c 100%);
  }
  .label {
    position: absolute;
    left: 60px;
    top: 1537px;
    width: 1080px;
    height: 1836px;
    overflow: hidden;
    background: linear-gradient(180deg, var(--label-blue-top) 0%, #1784cf 35%, var(--label-blue-light) 100%);
    box-shadow: 0 20px 60px rgba(0, 0, 0, 0.35);
  }
  .label-shapes {
    position: absolute;
    inset: 0;
    width: 1080px;
    height: 1836px;
  }
  .brand-name {
    position: absolute;
    left: 0;
    width: 1080px;
    top: 165px;
    margin: 0;
    text-align: center;
    font-weight: 800;
    font-size: 200px;
    line-height: 1;
    letter-spacing: -4px;
    color: var(--text-white);
  }
  .tagline {
    position: absolute;
    right: 111px;
    top: 388px;
    margin: 0;
    font-weight: 400;
    font-size: 36px;
    line-height: 44px;
    color: var(--text-white);
  }
  .tagline .synthetic { color: var(--accent-pink); font-style: italic; }
  .headline {
    position: absolute;
    left: 0;
    width: 1080px;
    top: 660px;
    margin: 0;
    text-align: center;
    font-style: italic;
    font-weight: 800;
    font-size: 44px;
    line-height: 52px;
    color: var(--text-white);
  }
  .slogan {
    position: absolute;
    left: 0;
    width: 1080px;
    top: 828px;
    margin: 0;
    text-align: center;
    font-style: italic;
    font-weight: 800;
    font-size: 62px;
    line-height: 76px;
    color: var(--text-white);
  }
  .slogan .code-prefix { color: var(--headline-red); }
  .benefits {
    position: absolute;
    left: 136px;
    top: 982px;
    margin: 0;
    padding: 0;
    list-style: none;
    font-style: italic;
    font-weight: 800;
    font-size: 37px;
    line-height: 62px;
    text-transform: uppercase;
    color: var(--bullet-blue);
  }
  .benefits li::before { content: "• "; }
  .volume {
    position: absolute;
    right: 108px;
    top: 1662px;
    margin: 0;
    font-style: italic;
    font-weight: 700;
    font-size: 56px;
    line-height: 68px;
    color: var(--text-white);
  }
</style>
</head>
<body>
<main class="canvas">
  <section class="label" aria-label="Lantern Stride QJ312 synthetic engine treatment label">
    <svg class="label-shapes" viewBox="0 0 1080 1836" aria-hidden="true">
      <defs>
        <linearGradient id="panel-fill" x1="0" y1="0" x2="0" y2="1">
          <stop offset="0" stop-color="#17181b"/>
          <stop offset="1" stop-color="#050506"/>
        </linearGradient>
        <linearGradient id="red-fill" x1="0" y1="0" x2="1" y2="0">
          <stop offset="0" stop-color="#e01a24"/>
          <stop offset="1" stop-color="#8a0a12"/>
        </linearGradient>
      </defs>
      <path d="M0 580 C 350 520, 750 470, 1080 450 L1080 475 C 750 495, 350 550, 0 610 Z" fill="var(--swoosh-white)" opacity="0.9"/>
      <path d="M0 605 C 350 545, 750 490, 1080 470 L1080 540 C 750 560, 350 630, 0 710 Z" fill="url(#red-fill)"/>
      <path d="M0 710 C 350 630, 750 560, 1080 540 L1080 1300 C 850 1400, 500 1500, 0 1540 Z" fill="url(#panel-fill)"/>
      <path d="M0 1540 C 500 1500, 850 1400, 1080 1300 L1080 1360 C 850 1450, 500 1560, 0 1600 Z" fill="url(#red-fill)"/>
      <path d="M0 1600 C 500 1560, 850 1450, 1080 1360 L1080 1410 C 850 1495, 500 1605, 0 1650 Z" fill="var(--swoosh-white)"/>
    </svg>

    <h1 class="brand-name">QJ312</h1>
    <p class="tagline"><span class="synthetic">Synthetic</span> Engine Treatment</p>

    <p class="headline">Don't dilute your synthetic oil<br>with a conventional based<br>engine treatment!</p>
    <p class="slogan">Use <span class="code-prefix">QJ</span>312 every time!</p>

    <ul class="benefits">
      <li>PTFE Protection</li>
      <li>Extend Engine Life</li>
      <li>Super Concentrated</li>
      <li>Reduce Engine Wear</li>
      <li>Improve Fuel Economy</li>
      <li>Reduces Heat and Friction</li>
      <li>Treats a Full 6 Quarts of Oil</li>
    </ul>

    <p class="volume">℮ 16 Fl Oz.</p>
  </section>
</main>
</body>
</html>
```